Residential Remodeling Contractor needs updated business card

I need a new design for my business card.
Name of the company is Brookfell Construction. I need a card that commands presence, strength, integrity. I have been in business for 28 years. I am a Residential Remodeling Contractor that covers all aspects of a residential remodel and build.

```html
<!DOCTYPE html>
<html lang="en">
<head>
<meta charset="UTF-8">
<title>Brookfell Construction – Business Card</title>
<link href="https://fonts.googleapis.com/css2?family=Poppins:wght@400;500;600&family=Marcellus+SC&display=swap" rel="stylesheet">
<style>
  :root {
    --backdrop: #1c1c1e;
    --card-blue: #1f3b7c;
    --card-blue-deep: #1a3270;
    --pattern-light: #2a4fa8;
    --ink: #ffffff;
    --rule: rgba(255,255,255,0.55);
  }
  * { margin: 0; padding: 0; box-sizing: border-box; }
  html, body { width: 1200px; height: 1108px; overflow: hidden; }
  body {
    background: var(--backdrop);
    font-family: 'Poppins', sans-serif;
    color: var(--ink);
    position: relative;
  }
  .card {
    position: absolute;
    top: 194px;
    width: 430px;
    height: 720px;
    border-radius: 26px;
    overflow: hidden;
  }
  .card--front {
    left: 150px;
    background: var(--card-blue);
    text-align: center;
    padding: 96px 36px 0;
  }
  .card--back {
    left: 620px;
    background: var(--card-blue-deep);
  }
  .brand-name {
    font-family: 'Poppins', sans-serif;
    font-weight: 600;
    font-size: 40px;
    line-height: 1.1;
    letter-spacing: 1px;
    color: var(--ink);
  }
  .brand-tagline {
    margin-top: 18px;
    font-size: 19px;
    font-weight: 500;
  }
  .person-name {
    margin-top: 58px;
    font-family: 'Marcellus SC', serif;
    font-size: 30px;
    letter-spacing: 1.5px;
  }
  .person-role {
    font-size: 17px;
    letter-spacing: 1px;
    text-transform: uppercase;
  }
  .icon-row {
    margin: 14px auto 8px;
    display: flex;
    align-items: center;
    gap: 8px;
    width: 300px;
  }
  .icon-row .rule { flex: 1; height: 1px; background: var(--rule); }
  .icon-tile {
    width: 30px; height: 30px;
    background: var(--ink);
    border-radius: 5px;
    display: flex; align-items: center; justify-content: center;
  }
  .contact-line { font-size: 19px; line-height: 1.45; }
  .divider { width: 300px; height: 1px; background: var(--rule); margin: 12px auto; }
  .address-line { font-size: 18px; line-height: 1.4; }
  .slogan {
    margin-top: 26px;
    font-size: 22px;
    font-weight: 500;
    line-height: 1.3;
  }
  .back-pattern {
    position: absolute; inset: 0;
    background:
      radial-gradient(ellipse at 70% 25%, var(--pattern-light) 0%, transparent 60%),
      linear-gradient(160deg, #22459a 0%, var(--card-blue-deep) 60%, #172c62 100%);
  }
  .back-brand {
    position: absolute;
    right: 44px;
    bottom: 150px;
    font-family: 'Poppins', sans-serif;
    font-weight: 600;
    font-size: 20px;
    line-height: 1.15;
    text-align: left;
    color: var(--ink);
  }
</style>
</head>
<body>
  <section class="card card--front">
    <div class="brand-name">Brookfell<br>Construction</div>
    <div class="brand-tagline">Residential Remodeling Contractor</div>

    <div class="person-name">Daniel Harlow</div>
    <div class="person-role">Managing Director</div>

    <div class="icon-row">
      <span class="rule"></span>
      <span class="icon-tile">
        <svg width="18" height="18" viewBox="0 0 24 24" fill="#1f3b7c" aria-label="Phone"><path d="M6.6 10.8a15.1 15.1 0 0 0 6.6 6.6l2.2-2.2c.3-.3.7-.4 1-.2 1.1.4 2.3.6 3.6.6.6 0 1 .4 1 1V20c0 .6-.4 1-1 1A17 17 0 0 1 3 4c0-.6.4-1 1-1h3.5c.6 0 1 .4 1 1 0 1.3.2 2.5.6 3.6.1.3 0 .7-.2 1z"/></svg>
      </span>
      <span class="icon-tile">
        <svg width="18" height="18" viewBox="0 0 24 24" fill="none" stroke="#1f3b7c" stroke-width="2" aria-label="Email"><rect x="3" y="5" width="18" height="14" rx="1"/><path d="M3 6l9 7 9-7"/></svg>
      </span>
      <span class="icon-tile">
        <svg width="18" height="18" viewBox="0 0 24 24" fill="none" stroke="#1f3b7c" stroke-width="2" aria-label="Website"><circle cx="12" cy="12" r="9"/><path d="M3 12h18M12 3c3 3 3 15 0 18M12 3c-3 3-3 15 0 18"/></svg>
      </span>
      <span class="rule"></span>
    </div>

    <div class="contact-line">044-555 010 274</div>
    <div class="contact-line">info@brookfellbuild.com</div>
    <div class="contact-line">www.brookfellbuild.com</div>
    <div class="divider"></div>
    <div class="address-line">421, Address line goes here</div>
    <div class="address-line">45452, Country Name</div>
    <div class="divider"></div>
    <div class="slogan">Building the Future,<br>Restoring the Past</div>
  </section>

  <section class="card card--back">
    <div class="back-pattern" role="img" aria-label="Repeating tone-on-tone company name pattern"></div>
    <div class="back-brand">Brookfell<br>Construction</div>
  </section>
</body>
</html>
```